Need Catering Menu designed - design that we want is attached

Hi,
We need a new catering menu designed for our cafe.
I have attached our coffee menu, we would like it to follow the same kind of layout.
It needs to be A4, and can be double sided.
I have attached a word doc of our catering menu, so this is what needs to be on the catering menu you produce.
Also, our contact details need to be on both sides of the menu:
Visit us instore to discuss catering options, or call 0438 672 914 or email martha@velbrisco.com.au
I have also attached our new logo which I'd like incorporated into the menu
Doctors/Nurses
Hospital staff
University Students
Catering

```html
<!DOCTYPE html>
<html lang="en">
<head>
<meta charset="utf-8">
<title>Ward Rounds – Catering Menu</title>
<link href="https://fonts.googleapis.com/css2?family=Courier+Prime:wght@400;700&family=Grand+Hotel&family=Oswald:wght@500&display=swap" rel="stylesheet">
<style>
  :root {
    --board: #141414;
    --chalk: #f4f1ea;
    --butter: #f6ef9e;
    --ink: #2b2526;
    --highlight: #f2e86a;
    --berry: #b3212b;
    --banana: #e9dfc0;
    --blueberry: #23263a;
  }
  * { margin: 0; padding: 0; box-sizing: border-box; }
  html, body { width: 857px; height: 1200px; overflow: hidden; }
  body {
    position: relative;
    background: radial-gradient(ellipse at 50% 40%, #242424 0%, var(--board) 70%, #0b0b0b 100%);
    color: var(--chalk);
    font-family: "Courier Prime", "Courier New", monospace;
  }
  .produce {
    position: absolute;
  }
  .produce--top-right {
    right: 0; top: 27px; width: 218px; height: 280px;
    background: radial-gradient(circle at 30% 35%, var(--berry) 0%, #7a1a20 35%, transparent 60%),
                radial-gradient(circle at 75% 70%, var(--banana) 0%, #c9bb92 35%, transparent 62%),
                radial-gradient(circle at 85% 20%, #d8d0b8 0%, transparent 40%),
                radial-gradient(circle at 60% 45%, var(--blueberry) 0%, transparent 45%);
    border-radius: 40% 0 0 50%;
  }
  .produce--bottom-left {
    left: 0; top: 973px; width: 133px; height: 187px;
    background: radial-gradient(circle at 35% 25%, var(--blueberry) 0%, transparent 55%),
                radial-gradient(circle at 45% 70%, var(--banana) 0%, #c9bb92 40%, transparent 68%);
    border-radius: 0 50% 50% 0;
  }
  .brand {
    position: absolute; left: 350px; top: 68px; width: 156px; height: 144px;
    background: var(--butter);
    display: flex; align-items: center; justify-content: center;
    text-align: center;
    font-family: "Oswald", sans-serif; font-weight: 500;
    font-size: 21px; letter-spacing: 2px; line-height: 1.15;
    color: var(--ink);
  }
  .title {
    position: absolute; left: 0; right: 0; top: 226px; text-align: center;
    font-family: "Grand Hotel", cursive; font-size: 50px; color: var(--chalk);
  }
  .title-rule {
    position: absolute; left: 318px; width: 220px; top: 292px;
    border-top: 4px dotted var(--chalk);
  }
  .menu-card {
    position: absolute; border: 2px solid var(--chalk);
  }
  .menu-card--breakfast { left: 205px; top: 344px; width: 440px; height: 372px; }
  .menu-card--tea { left: 209px; top: 771px; width: 440px; height: 246px; }
  .ribbon {
    position: absolute; top: -16px; left: 50%; transform: translateX(-50%);
    height: 32px; background: var(--board);
  }
  .ribbon svg { display: block; }
  .ribbon span {
    position: absolute; inset: 0; display: flex; align-items: center; justify-content: center;
    font-family: "Oswald", sans-serif; font-weight: 500; font-size: 17px; letter-spacing: 0.5px;
    color: var(--chalk);
  }
  .menu-list { list-style: none; position: absolute; left: 36px; right: 32px; }
  .menu-card--breakfast .menu-list { top: 64px; }
  .menu-card--tea .menu-list { top: 40px; }
  .menu-item {
    display: flex; align-items: baseline; font-size: 15px; line-height: 20.6px;
  }
  .menu-item .leader { flex: 1; border-bottom: 2px dotted var(--chalk); margin: 0 3px; transform: translateY(-4px); }
  .contact {
    position: absolute; left: 0; right: 0; top: 1040px; text-align: center;
    color: var(--highlight); font-size: 17px; line-height: 23px;
  }
  .contact strong { font-weight: 700; }
  .notes {
    position: absolute; left: 0; right: 0; top: 1094px; text-align: center;
    font-size: 11px; line-height: 16px; color: var(--chalk);
  }
</style>
</head>
<body>
  <div class="produce produce--top-right" role="img" aria-label="Photo of strawberries, blueberries, banana slices and a dish of granola"></div>
  <div class="produce produce--bottom-left" role="img" aria-label="Photo of blueberries and banana slices"></div>

  <div class="brand">WARD<br>ROUNDS</div>

  <h1 class="title">Catering Menu</h1>
  <div class="title-rule"></div>

  <section class="menu-card menu-card--breakfast">
    <div class="ribbon" style="width:274px">
      <svg width="274" height="32" viewBox="0 0 274 32"><polygon points="1,1 273,1 257,16 273,31 1,31 17,16" fill="var(--board)" stroke="var(--chalk)" stroke-width="2"/></svg>
      <span>BREAKFAST</span>
    </div>
    <ul class="menu-list">
      <li class="menu-item">Fruit Platter<i class="leader"></i>15</li>
      <li class="menu-item">Bacon Egg and Cheese Roll<i class="leader"></i>6.5</li>
      <li class="menu-item">Vegetarian Brekky Wrap<i class="leader"></i>6.5</li>
      <li class="menu-item">Ham and Cheese Croissant<i class="leader"></i>6</li>
      <li class="menu-item">Cheese and Tomato Croissant<i class="leader"></i>5.5</li>
      <li class="menu-item">Ham and Cheese French Toast<i class="leader"></i>6.5</li>
      <li class="menu-item">Assorted Yoghurts<i class="leader"></i>5.5</li>
      <li class="menu-item">Bircher Muesli<i class="leader"></i>5.5</li>
      <li class="menu-item">Chia Pudding<i class="leader"></i>5.5</li>
      <li class="menu-item">Granola and Yoghurt<i class="leader"></i>5.5</li>
      <li class="menu-item">Muffin<i class="leader"></i>4.5</li>
      <li class="menu-item">Mini Muffin<i class="leader"></i>2.5</li>
      <li class="menu-item">Juice<i class="leader"></i>3</li>
    </ul>
  </section>

  <section class="menu-card menu-card--tea">
    <div class="ribbon" style="width:300px">
      <svg width="300" height="32" viewBox="0 0 300 32"><polygon points="1,1 299,1 283,16 299,31 1,31 17,16" fill="var(--board)" stroke="var(--chalk)" stroke-width="2"/></svg>
      <span>MORNING &amp; AFTERNOON TEA</span>
    </div>
    <ul class="menu-list">
      <li class="menu-item">Fruit Platter<i class="leader"></i>15</li>
      <li class="menu-item">Muffin<i class="leader"></i>4.5</li>
      <li class="menu-item">Mini Muffin<i class="leader"></i>2.5</li>
      <li class="menu-item">Assorted Slices<i class="leader"></i>4</li>
      <li class="menu-item">Assorted Cookies from<i class="leader"></i>3</li>
      <li class="menu-item">Assorted Yoghurts<i class="leader"></i>5.5</li>
      <li class="menu-item">Chia Pudding<i class="leader"></i>5.5</li>
      <li class="menu-item">Banana Bread<i class="leader"></i>4.5</li>
      <li class="menu-item">Juice<i class="leader"></i>3</li>
    </ul>
  </section>

  <p class="contact">Visit us instore to discuss catering options, or call 0438 672 914<br>or <strong>email martha@velbrisco.com.au</strong></p>
  <p class="notes">*Cups/Plates/Serviettes can be provided at a charge of $1 per person<br>*Barista made coffee available</p>
</body>
</html>
```